Brenholt Timber Co website design

I have created an attached txt document with specifics of what I am looking for. The short version is that I am looking for a website design for a lumber yard/building materials store. They currently do not have a website other than a simple place holder. I have included several example websites of his direct competitors as well as made a note as to which one is the best example and the design he really likes. The txt document goes in depth as to navigation, points of interest and contact information. Unfortunately like most clients the logo files sucks. I am not sure why people don't have a good logo file.

```html
<!DOCTYPE html>
<html lang="en">
<head>
<meta charset="utf-8">
<title>Brenholt Timber Co</title>
<link rel="stylesheet" href="https://fonts.googleapis.com/css2?family=Nunito:wght@600;700;800&family=Nunito+Sans:wght@400;600;700&display=swap">
<style>
:root{
  --brown-dark:#4a1908;
  --brown:#5a1f0b;
  --green:#2b7a30;
  --green-dark:#23672a;
  --text:#4a4a4a;
  --muted:#777;
  --line:#d6d6d6;
  --white:#fff;
}
*{box-sizing:border-box;margin:0;padding:0}
html,body{width:1200px;height:3492px;overflow:hidden}
body{font-family:"Nunito Sans",sans-serif;color:var(--text);background:var(--white)}
a{color:inherit;text-decoration:none}
.wrap{width:1036px;margin:0 auto}

/* top bar */
.topbar{height:39px;background:var(--brown-dark);color:#e9dcd4;font-size:13px}
.topbar .wrap{display:flex;align-items:center;height:100%;gap:14px}
.topbar .item{display:flex;align-items:center;gap:5px}
.topbar svg{width:10px;height:12px}
.topbar .estimate{margin-left:auto;font-weight:700;color:#fff}

/* nav */
.nav{height:86px;background:var(--white)}
.nav .wrap{display:flex;align-items:center;height:100%}
.brand{display:flex;align-items:center;gap:10px}
.brand-mark{width:30px;height:30px;background:var(--green)}
.brand-name{font-family:"Nunito",sans-serif;font-weight:800;font-size:15px;line-height:15px;color:var(--green);text-transform:uppercase;width:140px}
.menu{margin-left:auto;display:flex;align-items:center;gap:44px;font-size:15px;color:#222}
.menu .contact{background:var(--green);color:#fff;padding:10px 32px;font-weight:600}

/* hero */
.hero{position:relative;height:460px}
.hero-photo{position:absolute;inset:0;background:linear-gradient(90deg,#2f5e44 0%,#3d6f5d 35%,#6d8a88 60%,#5d7c78 100%)}
.hero-text{position:relative;padding-top:118px;color:#fff}
.hero-kicker{font-size:19px;letter-spacing:.3px;text-transform:uppercase;font-weight:600}
.hero-title{font-family:"Nunito",sans-serif;font-weight:700;font-size:51px;line-height:64px;margin-top:8px}
.btn-outline{display:inline-flex;align-items:center;gap:12px;border:1.5px solid #fff;color:#fff;padding:8px 16px;font-size:16px;margin-top:22px;text-transform:uppercase}
.btn-outline svg{width:18px;height:12px}

/* search */
.search-card{position:relative;width:909px;height:171px;margin:-37px auto 0;background:#fff;box-shadow:0 4px 14px rgba(0,0,0,.14);padding:24px 26px}
.search-card h3{font-family:"Nunito",sans-serif;font-weight:700;font-size:27px;color:var(--brown)}
.search-card p{font-size:12px;color:var(--muted);margin-top:6px}
.search-row{display:flex;gap:12px;margin-top:18px}
.search-input{flex:1;height:50px;border:1px solid var(--line);font-size:14px;color:#888;display:flex;align-items:center;padding:0 14px}
.search-btn{width:159px;height:50px;background:var(--green);color:#fff;font-weight:700;font-size:16px;display:flex;align-items:center;justify-content:center}

/* sections */
.section{padding-top:61px}
.section h2{font-family:"Nunito",sans-serif;font-weight:700;font-size:40px;line-height:52px;color:var(--brown)}
.section .lead{font-size:19px;line-height:24px;color:#666;margin-top:9px}
.grid{display:grid;grid-template-columns:repeat(3,320px);column-gap:38px;row-gap:51px;margin-top:51px}
.card-img{height:228px;position:relative}
.card h4{font-family:"Nunito",sans-serif;font-weight:700;font-size:20px;line-height:28px;color:var(--brown);margin-top:16px}
.card p{font-size:14px;line-height:19px;color:var(--muted);margin-top:6px;width:290px}
.card-foot{display:flex;align-items:center;justify-content:space-between;margin-top:12px}
.btn{display:inline-flex;align-items:center;justify-content:center;width:130px;height:37px;background:var(--green);color:#fff;font-weight:700;font-size:15px}
.price{font-size:13px;color:var(--green-dark);font-weight:600}
.badge{position:absolute;left:16px;top:14px;background:var(--green);color:#fff;font-size:13px;font-weight:700;padding:3px 12px}
.products{padding-top:100px}

/* cta */
.cta{height:205px;margin-top:142px;position:relative}
.cta-photo{position:absolute;inset:0;background:linear-gradient(90deg,#7a3a1a 0%,#8a4b27 40%,#b06f3f 75%,#9a5a33 100%)}
.cta-inner{position:relative;width:1002px;margin:0 auto;padding-top:50px;color:#fff}
.cta h2{font-family:"Nunito",sans-serif;font-weight:700;font-size:40px;line-height:52px}
.cta .btn-light{display:inline-flex;align-items:center;gap:12px;background:#fff;color:#333;padding:9px 16px;font-size:16px;margin-top:15px;text-transform:uppercase}
.cta .btn-light svg{width:18px;height:12px}

/* footer */
.footer{height:370px;padding-top:100px}
.footer .wrap{display:flex}
.footer-brand{width:132px;display:flex;gap:8px;align-items:flex-start}
.footer-brand .brand-mark{width:26px;height:26px;flex:none}
.footer-brand span{font-family:"Nunito",sans-serif;font-weight:800;font-size:13px;line-height:15px;color:var(--green);text-transform:uppercase}
.fcol h5{font-family:"Nunito",sans-serif;font-weight:700;font-size:15px;color:var(--green);text-transform:uppercase;margin-bottom:16px}
.fcol li{list-style:none;font-size:15px;line-height:33px;color:#666}
.col-products{width:135px}
.col-services{width:181px}
.col-company{width:145px}
.col-resources{width:204px}
.contact-line{display:flex;gap:8px;font-size:15px;line-height:18px;color:#666;margin-bottom:14px;width:230px}
.contact-line svg{width:12px;height:14px;flex:none;margin-top:2px}
.bottombar{height:56px;background:var(--brown-dark);color:#cdb6a8;font-size:15px;display:flex;align-items:center;justify-content:center}
</style>
</head>
<body>

<div class="topbar">
  <div class="wrap">
    <div class="item"><svg viewBox="0 0 10 12"><path d="M5 0C2.2 0 0 2.1 0 4.8 0 8 5 12 5 12s5-4 5-7.2C10 2.1 7.8 0 5 0zm0 6.5A1.8 1.8 0 1 1 5 3a1.8 1.8 0 0 1 0 3.5z" fill="#6fbf5a"/></svg>BRENHOLT TIMBER CO 418 CEDAR RIDGE RD, PINE FALLS, MN 56011</div>
    <div class="item"><svg viewBox="0 0 12 12"><circle cx="6" cy="6" r="5" fill="none" stroke="#6fbf5a" stroke-width="1.3"/><path d="M6 3v3l2 1.3" fill="none" stroke="#6fbf5a" stroke-width="1.3"/></svg>MON - FRI 8AM - 5PM</div>
    <div class="estimate">Call for an estimate • (218) 555-0186</div>
  </div>
</div>

<header class="nav">
  <div class="wrap">
    <a class="brand" href="#"><span class="brand-mark"></span><span class="brand-name">Brenholt Timber Company</span></a>
    <nav class="menu">
      <a href="#">PRODUCTS</a><a href="#">SERVICES</a><a href="#">COMPANY</a><a href="#">RESOURCES</a>
      <a class="contact" href="#">CONTACT</a>
    </nav>
  </div>
</header>

<section class="hero">
  <div class="hero-photo" role="img" aria-label="Red flatbed delivery truck with a loader crane parked in the lumber yard, trees behind"></div>
  <div class="wrap hero-text">
    <div class="hero-kicker">Brenholt Timber Company</div>
    <h1 class="hero-title">A Reliable Partner<br>for Your Projects</h1>
    <a class="btn-outline" href="#">Find our more <svg viewBox="0 0 18 12"><path d="M0 6h16M11 1l5 5-5 5" fill="none" stroke="#6fcf5a" stroke-width="1.6"/></svg></a>
  </div>
</section>

<div class="search-card">
  <h3>What are you looking for?</h3>
  <p>Enter a short description of your service right here.</p>
  <div class="search-row">
    <div class="search-input">I want to look for...</div>
    <a class="search-btn" href="#">Search</a>
  </div>
</div>

<section class="section wrap">
  <h2>Our Services</h2>
  <p class="lead">Enter a short description of your service right here.</p>
  <div class="grid">
    <div class="card"><div class="card-img" role="img" aria-label="Store sales counter with staff" style="background:linear-gradient(160deg,#b98a5a,#d9cbb2 55%,#8b7a66)"></div><h4>Service Name</h4><p>Enter a short description of your service right here.</p><div class="card-foot"><a class="btn" href="#">Know More</a></div></div>
    <div class="card"><div class="card-img" role="img" aria-label="Stacked planed lumber boards" style="background:linear-gradient(135deg,#e0a070,#c97a48 50%,#a85a32)"></div><h4>Service Name</h4><p>Enter a short description of your service right here.</p><div class="card-foot"><a class="btn" href="#">Know More</a></div></div>
    <div class="card"><div class="card-img" role="img" aria-label="Log piles in a forest clearing" style="background:linear-gradient(180deg,#4d5d3a,#6b6a4c 50%,#a58a64)"></div><h4>Service Name</h4><p>Enter a short description of your service right here.</p><div class="card-foot"><a class="btn" href="#">Know More</a></div></div>
    <div class="card"><div class="card-img" role="img" aria-label="Covered lumber storage shed seen from a vehicle" style="background:linear-gradient(180deg,#4a3a30,#6e5a48 55%,#9a8a78)"></div><h4>Service Name</h4><p>Enter a short description of your service right here.</p><div class="card-foot"><a class="btn" href="#">Know More</a></div></div>
    <div class="card"><div class="card-img" role="img" aria-label="Delivery trucks parked in the yard" style="background:linear-gradient(180deg,#9fb2bd,#a6a9a4 45%,#b9b4aa)"></div><h4>Service Name</h4><p>Enter a short description of your service right here.</p><div class="card-foot"><a class="btn" href="#">Know More</a></div></div>
    <div class="card"><div class="card-img" role="img" aria-label="Store building with pickup trucks in front" style="background:linear-gradient(180deg,#7d8a98,#8d8272 50%,#c2b8a6)"></div><h4>Service Name</h4><p>Enter a short description of your service right here.</p><div class="card-foot"><a class="btn" href="#">Know More</a></div></div>
  </div>
</section>

<section class="section products wrap">
  <h2>Our Products</h2>
  <p class="lead">Enter a short description of your service right here.</p>
  <div class="grid">
    <div class="card"><div class="card-img" role="img" aria-label="Ends of stacked lumber boards" style="background:linear-gradient(135deg,#e2c29a,#c9a273 55%,#a57a4e)"><span class="badge">New</span></div><h4>Lumber</h4><p>Enter a short description of your service right here.</p><div class="card-foot"><a class="btn" href="#">Know More</a><span class="price">starts at $12.34</span></div></div>
    <div class="card"><div class="card-img" role="img" aria-label="Brick house with a tiled roof" style="background:linear-gradient(180deg,#2f6fb4,#8a7a70 45%,#b0583a 75%,#6a8a3a)"></div><h4>Roofing</h4><p>Enter a short description of your service right here.</p><div class="card-foot"><a class="btn" href="#">Know More</a><span class="price">starts at $12.34</span></div></div>
    <div class="card"><div class="card-img" role="img" aria-label="Wood flooring plank samples" style="background:linear-gradient(135deg,#e3a866,#c7844a 50%,#7a4424)"></div><h4>Flooring</h4><p>Enter a short description of your service right here.</p><div class="card-foot"><a class="btn" href="#">Know More</a><span class="price">starts at $12.34</span></div></div>
    <div class="card"><div class="card-img" role="img" aria-label="Tool belt with hand tools" style="background:linear-gradient(135deg,#6a3a1c,#a5602c 50%,#d5a040)"></div><h4>Tools</h4><p>Enter a short description of your service right here.</p><div class="card-foot"><a class="btn" href="#">Know More</a><span class="price">starts at $12.34</span></div></div>
    <div class="card"><div class="card-img" role="img" aria-label="Worker fitting insulation between roof rafters" style="background:linear-gradient(135deg,#c8a060,#e8e2d4 50%,#c9b27a)"></div><h4>Insulation</h4><p>Enter a short description of your service right here.</p><div class="card-foot"><a class="btn" href="#">Know More</a><span class="price">starts at $12.34</span></div></div>
    <div class="card"><div class="card-img" role="img" aria-label="Green siding on a house gable" style="background:linear-gradient(180deg,#6aa0d8,#b8cde0 35%,#8aa596 55%,#7a9486)"></div><h4>Siding</h4><p>Enter a short description of your service right here.</p><div class="card-foot"><a class="btn" href="#">Know More</a><span class="price">starts at $12.34</span></div></div>
  </div>
</section>

<section class="cta">
  <div class="cta-photo" role="img" aria-label="Close-up of stacked lumber boards in warm light"></div>
  <div class="cta-inner">
    <h2>Ready for your next project?</h2>
    <a class="btn-light" href="#">Find our more <svg viewBox="0 0 18 12"><path d="M0 6h16M11 1l5 5-5 5" fill="none" stroke="#333" stroke-width="1.6"/></svg></a>
  </div>
</section>

<footer class="footer">
  <div class="wrap">
    <div class="footer-brand"><span class="brand-mark"></span><span>Brenholt Timber Co</span></div>
    <div class="fcol col-products"><h5>Products</h5><ul><li>Flooring</li><li>Siding</li><li>Roofing</li><li>Lumber</li><li>Gypsum</li></ul></div>
    <div class="fcol col-services"><h5>Services</h5><ul><li>House Plans</li><li>Cabinet Design</li><li>Window Selection</li><li>Door Selection</li></ul></div>
    <div class="fcol col-company"><h5>Company</h5><ul><li>About</li><li>Careers</li><li>Policies</li><li>Testimonials</li></ul></div>
    <div class="fcol col-resources"><h5>Resources</h5><ul><li>Resource Categories</li><li>FAQS</li><li>Contractor Directory</li></ul></div>
    <div class="fcol"><h5>Contact Us</h5>
      <div class="contact-line"><svg viewBox="0 0 12 14"><rect x="2" y="1" width="8" height="12" rx="1.5" fill="none" stroke="#2b7a30" stroke-width="1.3"/></svg>(218) 555-0186</div>
      <div class="contact-line"><svg viewBox="0 0 10 12"><path d="M5 0C2.2 0 0 2.1 0 4.8 0 8 5 12 5 12s5-4 5-7.2C10 2.1 7.8 0 5 0zm0 6.5A1.8 1.8 0 1 1 5 3a1.8 1.8 0 0 1 0 3.5z" fill="#2b7a30"/></svg>Brenholt Timber Co 418 Cedar Ridge Rd, Pine Falls, Mn 56011</div>
    </div>
  </div>
</footer>

<div class="bottombar">Copyright © 2021 Harrowfield Build and Supply</div>

</body>
</html>
```